Buch-/E-Book-Cover Ratgeber Selbstliebe
Zielgruppe
Ich suche ein ansprechendes Cover-Design für mein E-Book. Es handelt sich um einen Ratgeber über Selbstliebe und meine Zielgruppe sind Frauen im Alter zwischen 18 und 40 Jahren.
Aufgabenstellung
Klare Designs, die das Thema des Ratgebers unterstreichen und nicht durch unnötige Details und unlesbare Verschnörkelungen ablenken. Die weibliche Zielgruppe sollte vor allem angesprochen werden, dies sollte auch in der Farbauswahl berücksichtigt werden. Das bedeutet helle Farbtöne wie rosa, rot, hellblau oder pastellgelb.
Die Umsetzung des Motivs überlasse ich der Kreativität des Designers. Es können sowohl Stockfotos von einer jungen Frau gewählt werden, die Freude ausstrahlt und sich wohl in ihrer Haut fühlt (wo vielleicht auch warmes Licht oder Sonnenschein auf dem Cover zu sehen sind) oder ein rein graphisches Bild aus zusammengesetzten Elementen, die eine junge Frau zeigen und ihre Beziehung zur Selbstliebe deutlich wird. Es muss nicht zwangsläufig ein Herz abgebildet werden, nur weil es das erste ist, was man vielleicht mit Liebe assoziiert, auch wenn ein kreativer Umgang mit dem Herz als Symbol eine durchaus ansprechende Wirkung haben kann. Wichtig wäre mir eine kreative Umsetzung im Bild, wodurch das Thema der 'Selbstliebe' sofort deutlich wird und den Käufer anspricht. Der Titel sollte genauso deutlich hervorstechen wie das zentrale Motiv. Außerdem sollte gleich erkennbar sein, dass es sich nicht um einen Roman, sondern um einen Ratgeber handelt. Daher bin ich an einer graphischen Aufbereitung genauso wie an einem Fotomotiv interessiert. Bereits existierende Cover zu einem ähnlichen Ratgeber- Thema, die ich ansprechend finde, füge ich im Anhang hinzu.
Bitte nicht die im Anhang eingefügten Dateien verwenden, da sie urheberrechtlich geschützt sind! Sie dienen nur als Interpretationsvorschlag.
Titel: Innere Ruhe finden
Untertitel: Wie aus kleinen Gewohnheiten jeden Tag neue Gelassenheit im Alltag wächst
Autorenname: Jana Roth
Der Buchrücken soll farblich an das Cover angepasst werden. Der Buchrückentext folgt noch im Anhang.
Das E-Book wird es auch als Paperback Buch geben. Der Umfang des Ra..

```html
<!DOCTYPE html>
<html lang="de">
<head>
<meta charset="utf-8">
<title>Innere Ruhe finden – Buchumschlag</title>
<link rel="stylesheet" href="https://fonts.googleapis.com/css2?family=Jost:wght@400&family=Arimo:wght@400&family=Parisienne&display=swap">
<style>
  :root {
    --pink-top: #f0abab;
    --pink-bottom: #d98f8f;
    --violet: #a8569b;
    --white: #ffffff;
    --title-white: #fbf1ef;
    --photo-skin: #e9b9a4;
    --photo-hair: #b0806a;
    --photo-shirt: #7c8468;
    --portrait-bg: #dfe6ef;
    --portrait-tone: #b98f7f;
  }
  * { margin: 0; padding: 0; box-sizing: border-box; }
  html, body { width: 1200px; height: 851px; overflow: hidden; }
  body { background: #fff; }

  .cover-spread {
    position: relative;
    width: 1200px;
    height: 851px;
    overflow: hidden;
    background: linear-gradient(180deg, var(--pink-top) 0%, var(--pink-bottom) 100%);
    font-family: "Jost", sans-serif;
    color: var(--white);
  }

  /* Back cover */
  .back-panel {
    position: absolute;
    left: 115px; top: 110px;
    width: 336px; height: 614px;
    background: var(--violet);
  }
  .author-portrait {
    position: absolute;
    left: 65px; top: 85px;
    width: 162px; height: 171px;
    background: radial-gradient(ellipse 45% 55% at 50% 60%, var(--portrait-tone) 0%, #8a7f8c 55%, var(--portrait-bg) 100%);
  }
  .back-subtitle {
    position: absolute;
    left: 241px; top: 199px;
    width: 200px;
    font-size: 14px;
    line-height: 18px;
  }
  .back-blurb {
    position: absolute;
    left: 150px; top: 305px;
    width: 270px;
    font-size: 13.6px;
    line-height: 18px;
    text-align: justify;
    hyphens: auto;
  }
  .back-signature {
    position: absolute;
    left: 318px; top: 572px;
    font-family: "Parisienne", cursive;
    font-size: 24px;
  }

  /* Spine */
  .spine {
    position: absolute;
    left: 557px; top: 0;
    width: 87px; height: 851px;
    background: var(--violet);
  }
  .spine-title, .spine-subtitle {
    position: absolute;
    transform: rotate(-90deg);
    white-space: nowrap;
  }
  .spine-title {
    left: 412px; top: 560px;
    width: 380px; height: 60px;
    font-family: "Parisienne", cursive;
    font-size: 43px;
    line-height: 60px;
    text-align: center;
  }
  .spine-subtitle {
    left: 443px; top: 188px;
    width: 320px; height: 46px;
    font-family: "Arimo", sans-serif;
    font-size: 13.5px;
    line-height: 20px;
  }
  .spine-author {
    position: absolute;
    left: 580px; top: 786px;
    font-family: "Arimo", sans-serif;
    font-size: 21px;
    line-height: 21px;
  }

  /* Front cover */
  .front-photo {
    position: absolute;
    left: 644px; top: 125px;
    width: 500px; height: 726px;
    background:
      radial-gradient(ellipse 28% 26% at 48% 28%, var(--photo-skin) 0%, rgba(233,185,164,0.6) 55%, rgba(176,128,106,0) 100%),
      radial-gradient(ellipse 40% 30% at 40% 26%, var(--photo-hair) 0%, rgba(176,128,106,0) 100%),
      radial-gradient(ellipse 55% 45% at 50% 78%, var(--photo-shirt) 0%, rgba(124,132,104,0.5) 60%, rgba(124,132,104,0) 100%);
  }
  .front-title {
    position: absolute;
    right: 32px; top: 22px;
    font-family: "Parisienne", cursive;
    font-weight: 400;
    font-size: 68px;
    line-height: 90px;
    color: var(--title-white);
    white-space: nowrap;
  }
  .front-subtitle {
    position: absolute;
    right: 31px; top: 121px;
    font-family: "Arimo", sans-serif;
    font-size: 15px;
    line-height: 21px;
    text-align: right;
  }
  .front-author {
    position: absolute;
    right: 37px; top: 780px;
    font-family: "Arimo", sans-serif;
    font-size: 22px;
  }
</style>
</head>
<body>
<main class="cover-spread">
  <section class="back-cover">
    <div class="back-panel"></div>
    <div class="author-portrait" role="img" aria-label="Porträtfoto der Autorin"></div>
    <p class="back-subtitle">Wie aus kleinen Gewohnheiten jeden Tag neue Gelassenheit im Alltag wächst</p>
    <p class="back-blurb">Lorem ipsum dolor sit amet, consetetur sadipscing elitr, sed diam nonumy eirmod tempor invidunt ut labore et dolore magna aliquyam erat, sed diam voluptua. At vero eos et accusam et justo duo dolores et ea rebum. Stet clita kasd gubergren, no sea takimata sanctus est Lorem ipsum dolor sit amet. Lorem ipsum dolor sit amet, consetetur sadipscing elitr, sed diam nonumy eirmod tempor invidunt ut labore et dolore magna aliquyam erat, sed diam voluptua. At vero eos et accusam et justo duo dolores et ea rebum. Stet clita kasd gubergren, no sea takimata sanctus est Lorem ipsum dolor sit amet.</p>
    <p class="back-signature">Jana Roth</p>
  </section>

  <section class="spine-area">
    <div class="spine"></div>
    <p class="spine-subtitle">Wie aus kleinen Gewohnheiten jeden Tag<br>neue Gelassenheit im Alltag wächst</p>
    <p class="spine-title">Innere Ruhe finden</p>
    <p class="spine-author">Jana<br>Roth</p>
  </section>

  <section class="front-cover">
    <div class="front-photo" role="img" aria-label="Foto einer lächelnden jungen Frau mit lockigem Haar, die sich selbst umarmt"></div>
    <h1 class="front-title">Innere Ruhe finden</h1>
    <p class="front-subtitle">Wie aus kleinen Gewohnheiten jeden Tag<br>neue Gelassenheit im Alltag wächst</p>
    <p class="front-author">Jana Roth</p>
  </section>
</main>
</body>
</html>
```